Book cover for an eBook about brix

We need a eBook cover for a series of eBooks. The current title is about the version control system "Brix". Therefor, the cover should relate to that topic.

However, we're planning to release quite a few more eBooks. We have a project called "klarsicht werkstatt" (german for "learn how to program"). Therefor the cover should be created with a general usability in mind. In fact, we would prefer a more general design that can be modified for other books. If graphic elements are used to express the topic visually, like an image on the cover, try to keep in mind that we can replace it for other topics. That would be perfect.

Colors should relate to our website and the logo. Don't go overboard with it, though. You can take a look at klarsichtwerkstatt.info. The cover should remind users of our identity.

Please integrate our logo (the text "klarsicht werkstatt" isn't a must). An AI-version of it is attached. Looking forward to your submission!

```html
<!DOCTYPE html>
<html lang="de">
<head>
<meta charset="utf-8">
<title>klarsicht werkstatt – eBook-Cover</title>
<link rel="stylesheet" href="https://fonts.googleapis.com/css2?family=Bebas+Neue&family=Montserrat:wght@400&display=swap">
<style>
  :root {
    --page: #ffffff;
    --purple-top: #6b2f9c;
    --purple-bottom: #4a2176;
    --blue-top: #2ba3de;
    --blue-bottom: #0c6cb3;
    --orange-top: #f8a65c;
    --orange-bottom: #f28a43;
    --photo-light: #f4f4f2;
    --photo-mid: #d9dad6;
    --photo-accent: #8cc63f;
    --title: #ffffff;
    --title-shade: #d8d8d8;
    --brand: #ffffff;
  }
  html, body {
    margin: 0;
    width: 1200px;
    height: 551px;
    overflow: hidden;
    background: var(--page);
  }
  .series {
    position: relative;
    width: 1200px;
    height: 551px;
  }
  .cover {
    position: absolute;
    top: 0;
    width: 391px;
    height: 548px;
    overflow: hidden;
  }
  .cover--purple { left: 0; height: 551px; background: linear-gradient(180deg, var(--purple-top), var(--purple-bottom)); }
  .cover--blue { left: 403px; background: linear-gradient(180deg, var(--blue-top), var(--blue-bottom)); }
  .cover--orange { left: 809px; background: linear-gradient(180deg, var(--orange-top), var(--orange-bottom)); }

  .cover__topic {
    position: absolute;
    left: 0;
    top: 0;
    width: 391px;
    height: 290px;
    filter: drop-shadow(0 4px 6px rgba(0,0,0,0.4));
  }
  .cover__title {
    position: absolute;
    left: 0;
    top: 302px;
    width: 100%;
    margin: 0;
    text-align: center;
    font-family: "Bebas Neue", "Arial Narrow", sans-serif;
    font-weight: 400;
    font-size: 56px;
    line-height: 50px;
    letter-spacing: 1px;
    color: var(--title);
    text-shadow: 0 3px 5px rgba(0,0,0,0.45);
  }
  .cover__title-line { display: block; }
  .cover__title-line--second { color: var(--title-shade); }

  .brand {
    position: absolute;
    left: 0;
    top: 446px;
    width: 100%;
    text-align: center;
    font-family: "Montserrat", Arial, sans-serif;
    font-weight: 400;
    color: var(--brand);
  }
  .brand__dot {
    display: block;
    width: 46px;
    height: 46px;
    margin: 0 auto 12px;
    border-radius: 50%;
    background: rgba(255,255,255,0.9);
  }
  .brand__name {
    display: block;
    font-size: 15px;
    line-height: 18px;
  }
</style>
</head>
<body>
<main class="series">

  <article class="cover cover--purple">
    <svg class="cover__topic" viewBox="0 0 391 290" role="img" aria-label="Themenfoto: Tastatur mit hervorgehobener grüner Taste">
      <defs>
        <linearGradient id="topic-fill-1" x1="0" y1="0" x2="1" y2="1">
          <stop offset="0" stop-color="#f4f4f2"/>
          <stop offset="0.45" stop-color="#e6e7e3"/>
          <stop offset="0.5" stop-color="#9ccd55"/>
          <stop offset="0.6" stop-color="#dfe0dc"/>
          <stop offset="1" stop-color="#cfd0cc"/>
        </linearGradient>
      </defs>
      <path d="M30 0 H362 L342 248 Q339 278 310 278 H80 Q51 278 48 248 Z" fill="url(#topic-fill-1)"/>
    </svg>
    <h1 class="cover__title">
      <span class="cover__title-line">Klarsicht</span>
      <span class="cover__title-line cover__title-line--second">Werkstatt</span>
    </h1>
    <div class="brand">
      <span class="brand__dot"></span>
      <span class="brand__name">klarsicht werkstatt</span>
    </div>
  </article>

  <article class="cover cover--blue">
    <svg class="cover__topic" viewBox="0 0 391 290" role="img" aria-label="Themenfoto: Tastatur mit hervorgehobener grüner Taste">
      <defs>
        <linearGradient id="topic-fill-2" x1="0" y1="0" x2="1" y2="1">
          <stop offset="0" stop-color="#f4f4f2"/>
          <stop offset="0.45" stop-color="#e6e7e3"/>
          <stop offset="0.5" stop-color="#9ccd55"/>
          <stop offset="0.6" stop-color="#dfe0dc"/>
          <stop offset="1" stop-color="#cfd0cc"/>
        </linearGradient>
      </defs>
      <path d="M30 0 H362 L342 248 Q339 278 310 278 H80 Q51 278 48 248 Z" fill="url(#topic-fill-2)"/>
    </svg>
    <h1 class="cover__title">
      <span class="cover__title-line">Klarsicht</span>
      <span class="cover__title-line cover__title-line--second">Werkstatt</span>
    </h1>
    <div class="brand">
      <span class="brand__dot"></span>
      <span class="brand__name">klarsicht werkstatt</span>
    </div>
  </article>

  <article class="cover cover--orange">
    <svg class="cover__topic" viewBox="0 0 391 290" role="img" aria-label="Themenfoto: Tastatur mit hervorgehobener grüner Taste">
      <defs>
        <linearGradient id="topic-fill-3" x1="0" y1="0" x2="1" y2="1">
          <stop offset="0" stop-color="#f4f4f2"/>
          <stop offset="0.45" stop-color="#e6e7e3"/>
          <stop offset="0.5" stop-color="#9ccd55"/>
          <stop offset="0.6" stop-color="#dfe0dc"/>
          <stop offset="1" stop-color="#cfd0cc"/>
        </linearGradient>
      </defs>
      <path d="M30 0 H362 L342 248 Q339 278 310 278 H80 Q51 278 48 248 Z" fill="url(#topic-fill-3)"/>
    </svg>
    <h1 class="cover__title">
      <span class="cover__title-line">Klarsicht</span>
      <span class="cover__title-line cover__title-line--second">Werkstatt</span>
    </h1>
    <div class="brand">
      <span class="brand__dot"></span>
      <span class="brand__name">klarsicht werkstatt</span>
    </div>
  </article>

</main>
</body>
</html>
```